WEB PAGES DESIGN

We need a web design for a new company called "NUBRA42". Our major business is that provide Internet Data Center solution, such as: rack/colocation, bandwidth, dedicated server, cloud server, CDN, and so on.
Requirements of Design:
1. Home page layout can refer to index-content.jpg in the attachments, but not limited.
2. According to match logo colors to design colors of web pages, Logo in the attachments.
3. The web contents of home page in image of the index-content.jpg.
4. The successful bidder will need to design three banner.
Industry/Entity Type
Business

```html
<!DOCTYPE html>
<html lang="en">
<head>
<meta charset="utf-8">
<title>NUBRA42 – IDC Solutions</title>
<link href="https://fonts.googleapis.com/css2?family=Roboto:ital,wght@0,300;0,400;0,500;0,700;1,400&display=swap" rel="stylesheet">
<style>
:root{
  --green:#8db229;
  --green-light:#b4d334;
  --dark:#2c2c2c;
  --ink:#333333;
  --muted:#666666;
  --band:#efefef;
  --line:#d9d9d9;
  --white:#ffffff;
}
*{margin:0;padding:0;box-sizing:border-box}
html,body{width:720px;height:1200px;overflow:hidden;background:var(--white)}
body{font-family:"Roboto",sans-serif;color:var(--ink);position:relative}
.abs{position:absolute}

.top-strip{left:0;top:0;width:720px;height:6px;background:#e8e8e8}
.brand{left:44px;top:14px;display:flex;align-items:center;gap:6px}
.brand-mark{width:14px;height:14px;background:var(--green)}
.brand-name{font-weight:700;font-size:15px;color:var(--dark);letter-spacing:1px}
.connect{left:512px;top:6px;width:160px;height:24px;background:#f3f3f3;display:flex;align-items:center;justify-content:flex-end;padding-right:8px;gap:4px;font-size:7px;color:var(--dark)}
.connect span{margin-right:6px}
.social{width:16px;height:16px;border-radius:50%;background:var(--green)}
.nav{left:276px;top:35px;display:flex;height:29px}
.nav a{font-size:7.5px;font-weight:500;color:var(--dark);text-decoration:none;display:flex;align-items:center;padding:0 11.5px}
.nav a.active{background:var(--green);color:var(--white);border-top:2px solid var(--dark);padding:0 13px}

.hero{left:0;top:64px;width:720px;height:278px;background:linear-gradient(100deg,#1d4f8f 0%,#3f7cc0 35%,#6aa3d8 60%,#a9cdea 100%)}
.hero-title{left:43px;top:64px;font-size:31px;font-weight:500;color:var(--green-light);letter-spacing:.5px}
.hero-text{left:44px;top:104px;width:300px;font-size:12px;font-weight:700;line-height:17.5px;color:var(--white)}
.btn-dark{background:var(--dark);color:var(--white);font-size:8px;display:flex;align-items:center;justify-content:center}
.hero-btn{left:45px;top:166px;width:78px;height:25px;font-size:9px}
.dots{display:flex;gap:4px}
.dot{width:8px;height:8px;border-radius:50%;background:var(--white)}
.dot.on{background:var(--green-light)}
.hero-dots{left:45px;top:253px}

.section-title{width:720px;text-align:center;font-size:19px;font-weight:500;color:var(--ink);letter-spacing:.5px}
.rule{left:180px;width:360px;height:2px;background:linear-gradient(90deg,transparent,#cfcfcf,transparent)}

.product{top:430px;width:150px;text-align:center}
.product svg{display:block;margin:0 auto}
.product h3{margin-top:9px;font-size:11px;font-weight:500;color:var(--green)}
.product p{margin:4px auto 0;width:144px;font-size:7px;line-height:12.8px;color:var(--muted)}
.product .btn-dark{width:50px;height:20px;margin:12px auto 0;font-size:7px}

.partners{left:0;top:662px;width:720px;height:197px;background:var(--band)}
.partner{top:86px;width:144px;height:52px;background:var(--white);border:1px solid #d8d8d8;display:flex;align-items:center;justify-content:center}
.partner i{display:block;width:96px;height:22px;background:#dde3ec;border-radius:2px}
.partners .dots{left:349px;top:169px}
.partners .dot{background:#555}
.partners .dot.on{background:var(--green)}

.block-title{font-size:19px;font-weight:500;color:var(--ink)}
.news{left:44px;width:240px;display:flex;gap:12px}
.date{width:28px;height:32px;background:#ececec;text-align:center;font-size:7px;color:var(--muted);padding-top:5px;flex:none}
.date b{display:block;font-size:12px;color:var(--dark)}
.news h4{font-size:7.5px;font-weight:400;color:var(--green);line-height:11px}
.news em{display:block;margin-top:5px;font-size:7px;color:var(--muted)}
.center-brand{left:318px;top:935px;width:84px;text-align:center}
.center-brand .sq{width:60px;height:60px;background:var(--green);margin:0 auto 10px}
.center-brand div.name{font-size:15px;font-weight:700;color:var(--dark);letter-spacing:1px}

.contact{left:452px;top:878px}
.c-name{left:468px;top:915px;font-size:8.5px;color:var(--green)}
.c-row{left:452px;display:flex;gap:8px;font-size:7.5px;color:var(--dark);line-height:11px}
.c-row svg{flex:none;margin-top:1px}
.c-row a{color:var(--green);text-decoration:none}
.c-rule{left:448px;top:1011px;width:228px;height:1px;background:var(--line)}
.support{top:1026px;width:80px;text-align:center;font-size:7.5px;font-weight:500;color:var(--dark)}
.support svg{display:block;margin:0 auto 8px}

.footer{left:0;top:1132px;width:720px;height:68px;background:var(--dark);color:#bbbbbb;font-size:7px}
.footer .copy{left:45px;top:24px;line-height:12px}
.footer .links{right:45px;top:30px}
.footer .links span{margin:0 7px;color:#777}
</style>
</head>
<body>

<div class="abs top-strip"></div>
<div class="abs brand"><div class="brand-mark"></div><div class="brand-name">NUBRA42</div></div>
<div class="abs connect"><span>CONNECT US:</span><i class="social"></i><i class="social"></i><i class="social"></i><i class="social"></i></div>
<nav class="abs nav">
  <a class="active">HOME</a><a>DEDICATED SERVERS</a><a>HOSTING</a><a>DATA CENTERS</a><a>ABOUT US</a><a>CONTACT US</a>
</nav>

<section class="abs hero" role="img" aria-label="Banner photo of server racks rising above clouds in a blue sky">
  <h1 class="abs hero-title">IDC SOLUTIONS</h1>
  <p class="abs hero-text">NUBRA42 Provides a Wide Range of highly specialized solutions that utilizes technology to transform your organizations.</p>
  <div class="abs btn-dark hero-btn">READ MORE</div>
  <div class="abs dots hero-dots"><i class="dot on"></i><i class="dot"></i><i class="dot"></i><i class="dot"></i></div>
</section>

<h2 class="abs section-title" style="top:369px">OUR&nbsp; PRODUCTS</h2>
<div class="abs rule" style="top:402px"></div>

<div class="abs product" style="left:43px">
  <svg width="94" height="107" viewBox="0 0 94 107"><polygon points="47,0 94,27 94,80 47,107 0,80 0,27" fill="#8db229"/>
    <g fill="#fff"><rect x="27" y="30" width="40" height="9" rx="4.5"/><rect x="27" y="43" width="40" height="9" rx="4.5"/><rect x="27" y="56" width="40" height="9" rx="4.5"/><rect x="46" y="65" width="2" height="10"/><rect x="24" y="75" width="46" height="2"/></g></svg>
  <h3>DEDICATED SERVERS</h3>
  <p>Lorem ipsum dolor sit amet, consectetur adipisicing eitseo eiusmod tempor incididunt ut labore et dolore magna aliqua.</p>
  <div class="btn-dark">MORE</div>
</div>
<div class="abs product" style="left:204px">
  <svg width="94" height="107" viewBox="0 0 94 107"><polygon points="47,0 94,27 94,80 47,107 0,80 0,27" fill="#8db229"/>
    <g fill="#fff"><polygon points="32,30 62,30 68,38 26,38"/><rect x="26" y="41" width="42" height="10"/><rect x="26" y="54" width="42" height="10"/><rect x="26" y="67" width="42" height="10"/></g></svg>
  <h3>SERVERS HOSTING</h3>
  <p>Lorem ipsum dolor sit amet, consectetur adipisicing eitseo eiusmod tempor incididunt ut labore et dolore magna aliqua.</p>
  <div class="btn-dark">MORE</div>
</div>
<div class="abs product" style="left:367px">
  <svg width="94" height="107" viewBox="0 0 94 107"><polygon points="47,0 94,27 94,80 47,107 0,80 0,27" fill="#8db229"/>
    <path d="M22 70 A25 25 0 1 1 72 70 Z" fill="#fff"/><path d="M30 66 A17 17 0 1 1 64 66 Z" fill="#8db229"/><polygon points="45,66 49,66 56,44" fill="#fff"/></svg>
  <h3>RACK &amp; BANDWIDTH</h3>
  <p>Lorem ipsum dolor sit amet, consectetur adipisicing eitseo eiusmod tempor incididunt ut labore et dolore magna aliqua.</p>
  <div class="btn-dark">MORE</div>
</div>
<div class="abs product" style="left:528px">
  <svg width="94" height="107" viewBox="0 0 94 107"><polygon points="47,0 94,27 94,80 47,107 0,80 0,27" fill="#8db229"/>
    <g fill="none" stroke="#fff" stroke-width="3"><circle cx="47" cy="40" r="7"/><circle cx="30" cy="64" r="7"/><circle cx="64" cy="64" r="7"/><path d="M43 46 L33 58 M51 46 L61 58 M37 64 H57"/></g></svg>
  <h3>RESELLER &amp; REFERRAL</h3>
  <p>Lorem ipsum dolor sit amet, consectetur adipisicing eitseo eiusmod tempor incididunt ut labore et dolore magna aliqua.</p>
  <div class="btn-dark">MORE</div>
</div>

<section class="abs partners">
  <h2 class="abs section-title" style="top:24px">OUR&nbsp; PARTNERS</h2>
  <div class="abs rule" style="top:58px"></div>
  <div class="abs partner" style="left:45px"><i></i></div>
  <div class="abs partner" style="left:207px"><i></i></div>
  <div class="abs partner" style="left:369px"><i></i></div>
  <div class="abs partner" style="left:531px"><i></i></div>
  <div class="abs dots"><i class="dot on"></i><i class="dot"></i></div>
</section>

<h2 class="abs block-title" style="left:44px;top:880px">LATEST NEWS</h2>
<div class="abs news" style="top:917px"><div class="date">Apr<b>03</b></div><div><h4>SED UT PERSPICIATIS UNDE OMNIS ISTE NATUS ERROR SIT VOLUPTATEM</h4><em>Read More</em></div></div>
<div class="abs news" style="top:969px"><div class="date">Apr<b>03</b></div><div><h4>SED UT PERSPICIATIS UNDE OMNIS ISTE NATUS ERROR SIT VOLUPTATEM</h4><em>Read More</em></div></div>
<div class="abs news" style="top:1022px"><div class="date">Apr<b>03</b></div><div><h4>SED UT PERSPICIATIS UNDE OMNIS ISTE NATUS ERROR SIT VOLUPTATEM</h4><em>Read More</em></div></div>
<div class="abs news" style="top:1074px"><div class="date">Apr<b>03</b></div><div><h4>SED UT PERSPICIATIS UNDE OMNIS ISTE NATUS ERROR SIT VOLUPTATEM</h4><em>Read More</em></div></div>

<div class="abs center-brand"><div class="sq"></div><div class="name">NUBRA42</div></div>

<h2 class="abs block-title contact">CONTACT US</h2>
<div class="abs c-name">NUBRA 42</div>
<div class="abs c-row" style="top:930px"><svg width="8" height="10" viewBox="0 0 8 10"><path d="M4 0a4 4 0 0 1 4 4c0 3-4 6-4 6S0 7 0 4a4 4 0 0 1 4-4z" fill="#333"/><circle cx="4" cy="4" r="1.4" fill="#fff"/></svg><i>417 Calder Lane<br>Dunmore, K12 7TR</i></div>
<div class="abs c-row" style="top:958px"><svg width="8" height="9" viewBox="0 0 8 9"><rect width="8" height="9" rx="1.5" fill="#333"/><path d="M2 2h2l-1 2 2 2 1-1v2H5C3 7 1 5 1 3z" fill="#fff"/></svg><span>Ph: <a>555-014-2290</a></span></div>
<div class="abs c-row" style="top:972px"><svg width="8" height="9" viewBox="0 0 8 9"><rect y="2" width="8" height="7" fill="#333"/><rect x="2" width="4" height="3" fill="#333"/><rect x="2" y="4" width="4" height="2" fill="#fff"/></svg><span>Fax: <a>555-014-2291</a></span></div>
<div class="abs c-row" style="top:986px"><svg width="8" height="8" viewBox="0 0 8 8"><rect y="1" width="8" height="6" fill="#333"/><path d="M0 1l4 3 4-3" stroke="#fff" fill="none"/></svg><span>Email: <a>info@nubra42.com</a></span></div>
<div class="abs c-rule"></div>

<div class="abs support" style="left:427px"><svg width="40" height="40" viewBox="0 0 40 40"><path d="M6 8h28v18H18l-8 7v-7H6z" fill="#333"/><circle cx="14" cy="17" r="2" fill="#fff"/><circle cx="20" cy="17" r="2" fill="#fff"/><circle cx="26" cy="17" r="2" fill="#fff"/></svg>LIVE CHAT</div>
<div class="abs support" style="left:517px"><svg width="40" height="40" viewBox="0 0 40 40"><circle cx="18" cy="18" r="14" fill="none" stroke="#333" stroke-width="2.5"/><path d="M11 18l5 5 9-10" fill="none" stroke="#333" stroke-width="3"/><text x="27" y="39" font-family="Roboto,sans-serif" font-size="9" font-weight="700" fill="#777">24</text></svg>SUPPORT ONLINE</div>
<div class="abs support" style="left:610px"><svg width="40" height="40" viewBox="0 0 40 40"><circle cx="20" cy="20" r="14" fill="#333"/></svg>TALKLINE</div>

<footer class="abs footer">
  <div class="abs copy">Copyright © 2015.CompanyName<br>All Right Reserved</div>
  <div class="abs links">Term of Services<span>|</span>Privacy Policy<span>|</span>Contact Us</div>
</footer>

</body>
</html>
```